Duel Business card

Want an edgy business card that shows both of our companies on each side of the card, OR both together with a cool design.

*Must be edgy: We have attached our two business logos. We are a bail bond and immigration bond company.

Would like the address on one side only.
Need Phone, cell, website, address, and Name

Company Name 1: Liberty Release Partners
www.libertyreleasepartners-example.com

Company Name 2: Crossway Custody Advocates
www.crosswaycustodyadvocates-example.com

These cards will need to be easily changeable so I can modify new employees

Target Market(s)

people in jail, takign imigrants out of jail and from being taken back to there country

Industry/Entity Type

Business

Requirements
Must have
• Include both logos attached

```html
<!DOCTYPE html>
<html lang="en">
<head>
<meta charset="utf-8">
<title>Liberty Release Partners &amp; Crossway Custody Advocates — Business Card</title>
<link rel="stylesheet" href="https://fonts.googleapis.com/css2?family=Open+Sans:wght@400;600&family=Ubuntu:ital,wght@0,700;1,700&display=swap">
<style>
  :root {
    --stage: #e6e7e8;
    --teal: #2cb6c6;
    --teal-deep: #229fae;
    --ink: #161616;
    --white: #ffffff;
    --paper: #f7f7f5;
    --brand-blue: #1f4fa8;
    --brand-red: #d8333a;
    --brand-gold: #f2c01e;
    --shadow: 0 18px 40px rgba(0,0,0,.28);
  }
  * { box-sizing: border-box; margin: 0; padding: 0; }
  html, body { width: 1200px; height: 900px; overflow: hidden; }
  body { background: var(--stage); font-family: "Open Sans", sans-serif; position: relative; }

  .card {
    position: absolute; left: 270px; width: 660px; height: 377px;
    box-shadow: var(--shadow); overflow: hidden;
  }
  .card--front { top: 60px; background: linear-gradient(160deg, var(--teal), var(--teal-deep)); color: var(--white); }
  .card--back { top: 463px; background: var(--paper); }

  /* front: brand marks */
  .brand { position: absolute; display: flex; align-items: center; gap: 10px; }
  .brand__dot { width: 34px; height: 34px; border-radius: 50%; flex: none; }
  .brand__name { font-family: "Ubuntu", sans-serif; font-weight: 700; font-size: 15px; line-height: 1.1; }
  .card--front .brand--custody { left: 26px; top: 24px; width: 170px; }
  .card--front .brand--custody .brand__dot { background: var(--white); }
  .card--front .brand--custody .brand__name { color: var(--white); }
  .card--front .brand--release { left: 210px; top: 24px; width: 170px; }
  .card--front .brand--release .brand__dot { background: var(--brand-blue); }
  .card--front .brand--release .brand__name { color: var(--brand-blue); }

  /* front: name ribbon */
  .ribbon { position: absolute; left: 0; top: 150px; width: 300px; height: 92px; }
  .ribbon svg { position: absolute; inset: 0; }
  .ribbon__text { position: absolute; left: 26px; top: 12px; }
  .ribbon__name { font-family: "Ubuntu", sans-serif; font-weight: 700; font-style: italic; font-size: 34px; line-height: 1.05; }
  .ribbon__title { font-family: "Ubuntu", sans-serif; font-weight: 700; font-style: italic; font-size: 22px; line-height: 1.2; }

  /* front: contact block */
  .contact { position: absolute; right: 24px; top: 100px; text-align: right; list-style: none; }
  .contact li { font-size: 16px; line-height: 25px; white-space: nowrap; }
  .contact li.contact__company { font-size: 17px; }
  .contact li.contact__web { font-size: 18px; }
  .contact small { font-size: 9px; opacity: .85; margin-left: 6px; display: inline-block; width: 44px; text-align: left; }

  /* back: large brand marks */
  .card--back .brand--custody { left: 40px; top: 60px; width: 250px; gap: 14px; }
  .card--back .brand--custody .brand__dot { width: 90px; height: 90px; background: var(--brand-red); }
  .card--back .brand--custody .brand__name { color: var(--brand-blue); font-size: 24px; }
  .card--back .brand--release { left: 280px; top: 170px; width: 350px; gap: 16px; }
  .card--back .brand--release .brand__dot { width: 70px; height: 70px; background: var(--brand-gold); }
  .card--back .brand--release .brand__name { color: var(--brand-blue); font-size: 40px; line-height: 1.05; }
</style>
</head>
<body>

  <section class="card card--front" aria-label="Business card front">
    <div class="brand brand--custody">
      <span class="brand__dot"></span>
      <span class="brand__name">Crossway Custody Advocates</span>
    </div>
    <div class="brand brand--release">
      <span class="brand__dot"></span>
      <span class="brand__name">Liberty Release Partners</span>
    </div>

    <div class="ribbon">
      <svg width="300" height="92" viewBox="0 0 300 92" aria-hidden="true">
        <polygon points="0,0 300,0 272,46 300,92 0,92" fill="var(--ink)"/>
      </svg>
      <div class="ribbon__text">
        <p class="ribbon__name">John Doe</p>
        <p class="ribbon__title">Title</p>
      </div>
    </div>

    <ul class="contact">
      <li class="contact__company">Liberty Release Partners</li>
      <li class="contact__company">Crossway Custody Advocates</li>
      <li>+000 123 456 789<small>telephone</small></li>
      <li>+000 123 456 789<small>cell</small></li>
      <li>123 John Rd. City, State, Zip<small>address</small></li>
      <li>www.libertyreleasepartners-example.com<small>web</small></li>
      <li class="contact__web">www.crosswaycustodyadvocates-example.com<small>web</small></li>
    </ul>
  </section>

  <section class="card card--back" aria-label="Business card back">
    <div class="brand brand--custody">
      <span class="brand__dot"></span>
      <span class="brand__name">Crossway Custody Advocates</span>
    </div>
    <div class="brand brand--release">
      <span class="brand__dot"></span>
      <span class="brand__name">Liberty Release Partners</span>
    </div>
  </section>

</body>
</html>
```